International professional tennis coach needs a book cover design

This is my 2nd published book, the first one was a #1 on the best seller. I'm looking for a world class book cover design for this new book. The name of my first book was 5 Baseline Habits to Unlock Your Rally Rhythm, located on Brimlow.com

The title of the new book:

Title: The Craft of Steady Rallies
Subtitle: Building a Tactical Margin by Way of Opponent Insight

I'm uploading our new CRAFT OF STEADY logo that I'd like for you to use as the centerpiece of the book design along with a 21st century design feel that incorporates what the book topic is below::

--> This book is about building competitive intelligence by using tennis data analytics to develop and expand a player's strategic advantage for match play. <--

The colors we would like to use are Blue, Yellow, and Green. These shades of these colors should be bold! (You will see the bold color examples of blues, yellows, and greens that I'm talking about in the logos that are attached here, especially the colors for my Tennis GridRally App logo.

I will upload the Tennis GridRally logo which should go somewhere on the back cover design (small size maybe in the bottom corner).

This book is revolutionary to the standard way of teaching tennis, it is based on a decade of recording and gathering tennis data analytics and then we created on-court practice games to develop better decision making in players for the competitive edge.

My websites are www.elevatedrillzone.com and www.craftofsteadyrallies.com

```html
<!DOCTYPE html>
<html lang="en">
<head>
<meta charset="utf-8">
<title>The Craft of Steady Rallies — Book Cover</title>
<link rel="stylesheet" href="https://fonts.googleapis.com/css2?family=Baloo+2:wght@700&family=Quicksand:wght@400;500&family=Bebas+Neue&family=Exo+2:wght@400&display=swap">
<style>
  :root {
    --stage: #f6cfa7;
    --paper: #f5f0ea;
    --lime: #97c41d;
    --ink: #3a3a3a;
    --title-ink: #4a4646;
    --blue: #1a87c9;
    --deep-blue: #0d86cc;
    --grass: #3f8a2a;
    --grass-light: #5aa83a;
  }
  * { box-sizing: border-box; margin: 0; padding: 0; }
  html, body { width: 1200px; height: 1000px; overflow: hidden; }
  body { background: var(--stage); position: relative; font-family: "Quicksand", sans-serif; }

  .cover { position: absolute; top: 71px; width: 500px; height: 705px; background: var(--paper); overflow: hidden; }
  .back-cover { left: 74px; width: 497px; }
  .front-cover { left: 612px; }

  /* Back cover */
  .tagline-band { position: absolute; top: 15px; left: 0; width: 492px; height: 46px; background: var(--lime);
    padding: 3px 0 0 35px; font-family: "Baloo 2", sans-serif; font-weight: 700; color: #fff; font-size: 15.5px; line-height: 20px; }
  .blurb { position: absolute; top: 72px; left: 35px; width: 420px; color: var(--ink); font-size: 9.6px; line-height: 13.6px; font-weight: 500; }
  .blurb p { margin-bottom: 7px; }
  .author { position: absolute; left: 35px; width: 432px; display: flex; gap: 9px; }
  .author-one { top: 323px; }
  .author-two { top: 471px; }
  .author-photo { flex: 0 0 97px; height: 115px; }
  .author-one .author-photo { background: linear-gradient(160deg, #6d6f6a, #3e4246 60%, #8a8f92); }
  .author-two .author-photo { background: linear-gradient(180deg, #9cc6e4, #a9b6a4 55%, #3b4450); }
  .author-bio { font-size: 9.6px; line-height: 13.6px; color: var(--ink); font-weight: 500; }
  .author-name { color: var(--blue); font-family: "Baloo 2", sans-serif; font-weight: 700; font-size: 10.5px; }
  .app-mark { position: absolute; top: 600px; left: 45px; width: 110px; display: flex; flex-direction: column; align-items: center; gap: 3px; }
  .app-dot { width: 26px; height: 26px; border-radius: 50%; background: var(--deep-blue); }
  .app-name { font-weight: 500; font-size: 9px; color: var(--deep-blue); }
  .web-links { position: absolute; top: 655px; left: 25px; width: 130px; text-align: center; font-size: 8px; line-height: 10px; color: #222; font-weight: 500; }
  .base-rule { position: absolute; top: 682px; left: 0; width: 492px; height: 5px; background: var(--lime); }

  /* Front cover */
  .court-top { position: absolute; top: 0; left: 0; width: 500px; height: 92px;
    background: linear-gradient(90deg, var(--grass-light), var(--grass)); }
  .court-bottom { position: absolute; top: 575px; left: 0; width: 500px; height: 130px;
    background: linear-gradient(180deg, var(--grass-light), var(--grass)); }
  .book-title { position: absolute; top: 136px; left: 0; width: 500px; text-align: center;
    font-family: "Bebas Neue", sans-serif; color: var(--title-ink); font-size: 92px; line-height: 88px; letter-spacing: 1px; }
  .title-rule { position: absolute; top: 318px; left: 58px; width: 384px; height: 3px; background: var(--blue); }
  .subtitle { position: absolute; top: 323px; left: 0; width: 500px; text-align: center;
    font-family: "Exo 2", sans-serif; color: var(--blue); font-size: 24px; line-height: 31px; }
  .authors { position: absolute; top: 466px; left: 0; width: 500px; text-align: center;
    font-family: "Bebas Neue", sans-serif; color: var(--blue); font-size: 29px; line-height: 28px; letter-spacing: 0.5px; }
</style>
</head>
<body>

<section class="cover back-cover">
  <div class="tagline-band">A practical guide on how to win more matches by<br>becoming a more efficient and effective competitor.</div>
  <div class="blurb">
    <p>As a tennis player you have the ability to play better matches and win more of them. The Craft of Steady Rallies gives you a system to improve. We start with the individual game of the set itself. Our system examines your physical and mental progression, enabling you to upgrade your movement and performance from shot to shot and point to point. Our system seamlessly integrates the technical (physical) aspects with the tactical (mental/emotional) components, providing a comprehensive approach to elevate this performance.</p>
    <p>We aim to give you much more than how to hit great shots. Irrespective of your current skill level, we will provide you with a detailed strategic and tactical plan to enhance your performance, leading to improved results and increased success in your matches.</p>
    <p>The Craft of Steady Rallies emphasizes the importance of shifting focus from oneself to the opponent, encouraging players to analyze and understand their adversaries. By bringing the opponent back to the forefront of their thinking, the player creates the best possible context in which to improve as a competitor.</p>
    <p>In this book, we present a groundbreaking approach to tennis data analytics that seamlessly integrates match performance with practice sessions, and vice versa.</p>
  </div>

  <div class="author author-one">
    <div class="author-photo" role="img" aria-label="Portrait photo of coach Marlow Kestrel on court"></div>
    <p class="author-bio"><span class="author-name">Marlow Kestrel</span> is regarded as one of the leading strategy and tactical coaches in the world today. He is the Creator of Tennis GridRally, the world's first Tennis Tracking App that maps and charts match play based on the rally length of a point. Marlow is a Best Selling Author of the book "5 Baseline Habits to Unlock Your Rally Rhythm" and the Co-Founder of The Craft of Steady Rallies promoting coach, player, and parent development. He is often sought after by coaches around the world to design the practice court in a way that revolutionizes a player's mindset to successfully negotiate the pressures of competitive match play.</p>
  </div>

  <div class="author author-two">
    <div class="author-photo" role="img" aria-label="Portrait photo of coach Owen Talbot outdoors"></div>
    <p class="author-bio"><span class="author-name">Owen Talbot</span> is a writer and tennis coach. He is a Co-Founder at The Craft of Steady Rallies and has been working to create a theoretical framework for tennis players of all levels to improve. Owen studies the forces that act on the player during a tennis match (both internal and external) and works with players to meet the challenge these forces represent. He runs online and on court programs designed specifically to improve a player's Competitive Intelligence.</p>
  </div>

  <div class="app-mark">
    <span class="app-dot"></span>
    <span class="app-name">Tennis GridRally</span>
  </div>
  <div class="web-links">www.elevatedrillzone.com<br>www.craftofsteadyrallies.com</div>
  <div class="base-rule"></div>
</section>

<section class="cover front-cover">
  <div class="court-top" role="img" aria-label="Photo of a green grass tennis court with a white line"></div>
  <h1 class="book-title">The Craft of<br>Steady Rallies</h1>
  <div class="title-rule"></div>
  <p class="subtitle">BUILDING A TACTICAL MARGIN<br>BY WAY OF OPPONENT INSIGHT</p>
  <p class="authors">Marlow Kestrel<br>&amp; Owen Talbot</p>
  <div class="court-bottom" role="img" aria-label="Photo of a blue tennis racket and yellow ball lying on a grass court"></div>
</section>

</body>
</html>
```